Brochure for donors of the annual fund for a school

We need a brochure for a fundraising effort.

I have attached:
• two photos which he might want to decide which is best for the outside of the brochure. If he decides to use the group photo, I would like him to crop out the left two people.
• stationery photos to get an idea of the colors we use and our font…
• The Every Family by Spring logo
• School logos

I have attached a copy of the ashgrove school brochure for the outside copy (read instructions below) and for a sense of artistic sensibility that we are looking for. The pledge form on the inside of the ashgrove school brochure needs to be added as well.

Our colors that we use in the website are:
Green: 66A040
Blue: 4B63AE
Grey: ACA095
Brown Grey 8C7D70

He should look at our website for the colors: https://www.mapleridgeacademy.example/page

The copy is as follows:

Draft for the brochure: (For the inside)
Maple Ridge has been nurturing minds and hearts since its founding in 1987. Rooted in the Quaker values of simplicity, peace, community, equality, and stewardship, MRA welcomes families of all backgrounds into a learning environment that supports each student’s intellectual and personal growth. Our faculty and staff are dedicated educators, helping children develop into caring, contributing, and successful members of their communities, in high school and beyond.
The distinctive elements that make a MRA education so rewarding for our students and families require a significant financial investment. And yet the revenue that MRA receives from tuition each year covers less than 75% of the cost of educating each student.
To close this gap, each year the extended MRA community comes together in support of the annual Lantern Fund, providing critical dollars needed by our teachers and students, from books and classroom materials to special assemblies and field trips. Lantern Fund gifts make it all possible.
This year, MRA is striving for an ambitious goal of securing 100% parent participation in 100 days. Your family’s contribution to the Lantern Fund will go a long way in helping MRA demonstrate to the wider community the commitment of our current parents, inspiring generosity from other friends of the school.
We hope you will make your gift or pledge, using the enclosed form, before December 31, 2017. Prefer to make a gift or pledge online? Please visit us at: https://www.mapleridgeacademy.example/page/support-mra

INSTRUCTIONS:
Attached is the PDF files of a brochure to use as a guideline. We are hoping to keep everything for the brochure is the same, and to make the following changes:
• Modify the text on the lefthand side (See attached text)
• Change the colors of the brochure to MRA colors (Green: 66A040; Blueish purple: 4B63AE, light grey ACA095)
• Remove the logo on the front (of the person holding the "world") and replace it with the hands reaching to 100 graphic design
• Wherever the text says "Ashgrove Vale School", of course please change it to "Maple Ridge Academy"
• Wherever the text says "Annual Fund" please change it to "Lantern Fund"
• The Annual Fund year (Lantern Fund Year) is 2017-18
• On the inside right most column, please change the phone number under PLEDGE to 555-217-4830 ext. 42
• The address on the back should be MRA's address, phone, and website information

Target Market(s)

Donors with money and class.

Industry/Entity Type

School

Requirements
Must have
• Easy to read. High end design.
Should not have
• Clip art

```html
<!DOCTYPE html>
<html lang="en">
<head>
<meta charset="utf-8">
<title>Lantern Fund 2017-18 – Maple Ridge Academy</title>
<link rel="stylesheet" href="https://fonts.googleapis.com/css2?family=Source+Sans+3:ital,wght@0,300;0,400;0,600;0,700;1,400&display=swap">
<style>
:root{
  --brown-grey:#8C7D70;
  --green:#66A040;
  --ink:#4a4440;
  --label:#9a928b;
  --rule:#b9b1aa;
  --paper:#ffffff;
}
*{margin:0;padding:0;box-sizing:border-box}
html,body{width:1200px;height:994px;overflow:hidden;background:var(--paper)}
body{font-family:"Source Sans 3",Arial,sans-serif;color:var(--ink);position:relative}

.intro-panel{position:absolute;left:0;top:57px;width:396px;height:937px;background:var(--brown-grey);color:#fff;overflow:hidden}
.intro-title{position:absolute;left:30px;top:42px;font-weight:300;font-size:27px;letter-spacing:.1px;white-space:nowrap}
.intro-tagline{position:absolute;left:30px;top:76px;font-style:italic;font-size:16px;font-weight:400}
.intro-copy{position:absolute;left:30px;top:116px;width:340px;font-size:14px;line-height:18.6px;text-align:justify;font-weight:400}
.intro-copy p{margin-bottom:18.6px}
.intro-copy p:last-child{margin-bottom:0;text-align:left}
.intro-copy .web{font-weight:700;overflow-wrap:anywhere}

.hero-photo{position:absolute;left:396px;top:57px;width:804px;height:240px}

.gift-form{position:absolute;left:427px;top:0;width:340px}
.form-title{position:absolute;top:306px;left:0;color:var(--green);font-size:19.5px;font-weight:600;white-space:nowrap}
.form-sub{position:absolute;top:332px;left:0;font-size:14px;white-space:nowrap}
.check-line{position:absolute;left:0;font-size:13.5px;font-weight:600;white-space:nowrap;display:flex;align-items:center;gap:8px}
.box{display:inline-block;width:11px;height:11px;border:1px solid var(--ink);flex:none}
.field{position:absolute;left:0;width:336px;border-bottom:1px solid var(--rule);font-size:13px;color:var(--label);padding-bottom:6px;height:26px}
.field.split span+span{margin-left:62px}
.amount{position:absolute;left:0;top:411px;width:336px;height:24px;border-bottom:1px solid var(--rule);font-size:14px}
.fund-name{position:absolute;left:0;top:441px;font-size:12px;font-weight:700}
.blank{position:absolute;left:0;width:336px;border-bottom:1px solid var(--rule)}

.side-form{position:absolute;left:818px;top:0;width:346px;font-size:12.4px}
.side-head{position:absolute;left:0;color:var(--green);font-weight:700;font-size:13.5px;letter-spacing:.3px}
.row{position:absolute;left:14px;width:332px;white-space:nowrap;display:flex;align-items:center;gap:6px}
.row .line{flex:1;border-bottom:1px solid var(--rule);height:12px}
.row .box{width:10px;height:10px}
.row.wrap{white-space:normal;align-items:flex-start;line-height:16px}
.row.wrap .box{margin-top:3px}
.sig-line{position:absolute;left:14px;width:332px;border-bottom:1px solid var(--rule)}
.digits{position:absolute;left:14px;display:flex;gap:10px}
.digit-group{display:flex}
.digit-group i{display:block;width:11px;height:17px;border-left:1px solid var(--rule);border-bottom:1px solid var(--rule);margin-right:3px}
.digit-group i:last-child{border-right:1px solid var(--rule);margin-right:0}
.short{display:inline-block;border-bottom:1px solid var(--rule);height:12px}
</style>
</head>
<body>

<section class="intro-panel">
  <h1 class="intro-title">Annual Lantern Fund 2017-18</h1>
  <p class="intro-tagline">Nurturing minds and hearts</p>
  <div class="intro-copy">
    <p>Maple Ridge has been nurturing minds and hearts since its founding in 1987. Rooted in the Quaker values of simplicity, peace, community, equality, and stewardship, MRA welcomes families of all backgrounds into a learning environment that supports each student’s intellectual and personal growth. Our faculty and staff are dedicated educators, helping children develop into caring, contributing, and successful members of their communities, in high school and beyond.</p>
    <p>The distinctive elements that make a MRA education so rewarding for our students and families require a significant financial investment. And yet the revenue that MRA receives from tuition each year covers less than 75% of the cost of educating each student.</p>
    <p>To close this gap, each year the extended MRA community comes together in support of the annual Lantern Fund, providing critical dollars needed by our teachers and students, from books and classroom materials to special assemblies and field trips. Lantern Fund gifts make it all possible.</p>
    <p>This year, MRA is striving for an ambitious goal of securing 100% parent participation in 100 days. Your family’s contribution to the Lantern Fund will go a long way in helping MRA demonstrate to the wider community the commitment of our current parents, inspiring generosity from other friends of the school.</p>
    <p>We hope you will make your gift or pledge, using the enclosed form, before December 31, 2017.</p>
    <p>Prefer to make a gift or pledge online? Please visit us at: <span class="web">www.mapleridgeacademy.example/page/support-mra</span></p>
  </div>
</section>

<svg class="hero-photo" viewBox="0 0 804 240" role="img" aria-label="Photo of a teacher and two students crouching outdoors, examining a small object together">
  <defs>
    <linearGradient id="photoTone" x1="0" y1="0" x2="1" y2="1">
      <stop offset="0" stop-color="#a9a59e"/>
      <stop offset=".45" stop-color="#7d8494"/>
      <stop offset=".75" stop-color="#5d6a8e"/>
      <stop offset="1" stop-color="#9a968f"/>
    </linearGradient>
  </defs>
  <path d="M0 0H804V180Q560 232 300 226Q130 222 0 236Z" fill="url(#photoTone)"/>
  <path d="M0 240Q150 222 330 232Q580 240 804 188" fill="none" stroke="#c9c3bd" stroke-width="1.2"/>
</svg>

<section class="gift-form">
  <h2 class="form-title">Please Make a Gift Today</h2>
  <p class="form-sub">to Maple Ridge Academy’s Annual Lantern Fund</p>
  <div class="check-line" style="top:390px"><span class="box"></span>I/We would like to make a gift of</div>
  <div class="amount">$</div>
  <div class="fund-name">MRA’s Annual Lantern Fund</div>
  <div class="field" style="top:478px">Name(s)</div>
  <div class="field" style="top:524px">Address</div>
  <div class="field" style="top:570px">City</div>
  <div class="field split" style="top:616px"><span>State</span><span>Zip Code</span></div>
  <div class="field" style="top:662px">Home Phone</div>
  <div class="field" style="top:708px">Business Phone</div>
  <div class="field" style="top:754px">Email Address(es)</div>
  <div class="check-line" style="top:821px"><span class="box"></span>Please recognize this gift under the name(s)</div>
  <div class="blank" style="top:866px"></div>
  <div class="blank" style="top:896px"></div>
  <div class="check-line" style="top:918px"><span class="box"></span>This gift is anonymous</div>
</section>

<section class="side-form">
  <h3 class="side-head" style="top:305px">PAYMENT</h3>
  <div class="row" style="top:325px;font-weight:600">Total gift amount $<span class="line"></span></div>
  <div class="row" style="top:348px"><span class="box"></span>Credit/Debit Card <span class="box" style="margin-left:8px"></span>Cash</div>
  <div class="row" style="top:368px"><span class="box"></span>Check (made payable to Maple Ridge Academy)</div>

  <h3 class="side-head" style="top:401px">CREDIT CARD INFO</h3>
  <div class="row" style="top:422px">Name as it appears on card</div>
  <div class="sig-line" style="top:456px"></div>
  <div class="row" style="top:465px">Account Number</div>
  <div class="digits" style="top:492px">
    <span class="digit-group"><i></i><i></i><i></i><i></i></span>
    <span class="digit-group"><i></i><i></i><i></i><i></i></span>
    <span class="digit-group"><i></i><i></i><i></i><i></i></span>
    <span class="digit-group"><i></i><i></i><i></i><i></i></span>
  </div>
  <div class="row" style="top:520px">Expiration Date</div>
  <div class="digits" style="top:546px">
    <span class="digit-group"><i></i><i></i><i></i><i></i></span>
  </div>
  <div class="row" style="top:575px">Signature</div>
  <div class="sig-line" style="top:611px"></div>

  <h3 class="side-head" style="top:625px">PLEDGE</h3>
  <div class="row" style="top:648px">I will make the following gift to Maple Ridge Academy:</div>
  <div class="row wrap" style="top:665px"><span class="box"></span><span>Stock Gift (please call 555-217-4830 ext. 42 with stock gift details)</span></div>
  <div class="row" style="top:701px"><span class="box"></span>Foundation Gift</div>
  <div class="row" style="top:719px"><span class="box"></span>Matching Gift (please enclose matching gift form)</div>
  <div class="row" style="top:738px"><span class="box"></span>Other<span class="line"></span></div>
  <div class="row" style="top:757px">Amount <span class="short" style="width:96px"></span> Date<span class="line"></span></div>
  <div class="row" style="top:776px">Amount <span class="short" style="width:96px"></span> Date<span class="line"></span></div>
  <div class="row" style="top:796px"><span class="box"></span>Please invoice me for these payments.</div>
  <div class="row" style="top:826px">Signature (required for all pledge gifts)</div>
  <div class="sig-line" style="top:868px"></div>

  <h3 class="side-head" style="top:885px">INFORMATION</h3>
  <div class="row" style="top:905px">Please send me more information about:</div>
  <div class="row" style="top:923px"><span class="box"></span>Stock and securities gifts</div>
  <div class="row" style="top:941px"><span class="box"></span>Foundation and charitable trust gifts</div>
  <div class="row" style="top:959px"><span class="box"></span>Providing for Maple Ridge Academy in my will</div>
</section>

</body>
</html>
```